81M business card

I need a business card for a life sciences consulting firm I started. The company name is 81M and the logo is attached. I am looking for something edgey and current but different from the blah standard business card.

Industry/Entity Type

Business

Requirements
Nice to have
• Both sides

```html
<!DOCTYPE html>
<html lang="en">
<head>
<meta charset="utf-8">
<title>81M LLC – Business Card</title>
<link href="https://fonts.googleapis.com/css2?family=Exo+2:ital,wght@0,300;0,400;0,500;1,300;1,400&display=swap" rel="stylesheet">
<style>
  :root{
    --bg:#e9e9ea;
    --navy-dark:#16235c;
    --navy:#233a8c;
    --navy-text:#2b3a8a;
    --band:#f4f4f6;
    --stripe:#d9dbee;
    --grey-text:#7a7f8c;
    --ink:#2a2d36;
    --orange:#f05a24;
    --orange-mid:#f5933a;
    --orange-light:#f7a84a;
    --title-ink:#5a2a0e;
    --card-white:#fbfbfb;
  }
  *{box-sizing:border-box;margin:0;padding:0}
  html,body{width:1200px;height:1000px;overflow:hidden}
  body{
    background:var(--bg);
    font-family:"Exo 2",sans-serif;
    display:flex;flex-direction:column;align-items:center;justify-content:center;gap:56px;
  }
  .card{
    width:760px;height:434px;position:relative;overflow:hidden;
    box-shadow:0 10px 28px rgba(0,0,0,.18);
  }

  /* ---------- Back side ---------- */
  .card--back{
    background:radial-gradient(ellipse at 55% 35%, var(--navy) 0%, var(--navy-dark) 85%);
  }
  .card--back svg.band{position:absolute;inset:0}
  .card--back .brand{position:absolute;left:40px;top:164px}
  .card--back .url{
    position:absolute;right:70px;bottom:78px;
    color:#dfe3f5;font-weight:300;font-size:19px;letter-spacing:.5px;
  }

  /* ---------- Brand lockup ---------- */
  .brand{display:flex;align-items:center;gap:20px}
  .brand__dot{width:76px;height:76px;border-radius:50%;background:var(--navy-text);flex:none}
  .brand__text{display:flex;flex-direction:column}
  .brand__name{
    font-weight:500;font-size:66px;line-height:1;color:var(--navy-text);letter-spacing:2px;
    white-space:nowrap;
  }
  .brand__tagline{
    font-weight:400;font-size:12.5px;color:var(--grey-text);letter-spacing:.6px;margin-top:4px;
    white-space:nowrap;
  }

  /* ---------- Front side ---------- */
  .card--front{background:var(--card-white)}
  .card--front .brand{position:absolute;left:44px;top:48px}
  .contact{position:absolute;color:var(--ink);font-weight:400;font-size:19px;line-height:1.3;white-space:nowrap}
  .contact--address{left:46px;top:214px}
  .contact--direct{left:480px;top:258px}
  .id-band{position:absolute;left:0;top:340px;height:52px;display:flex}
  .id-band__name{
    width:280px;height:52px;
    background:linear-gradient(90deg,var(--orange),#f27a2e);
    color:#fff;font-weight:300;font-style:italic;font-size:27px;white-space:nowrap;
    display:flex;align-items:center;padding-left:50px;
  }
  .id-band__title{
    width:160px;height:52px;background:var(--orange-mid);
    color:var(--title-ink);font-size:17px;font-weight:400;white-space:nowrap;
    display:flex;align-items:center;padding-left:16px;
  }
  .tiles{position:absolute;left:452px;top:340px;display:flex;gap:10px}
  .tiles span{width:50px;height:52px;background:var(--orange-light)}
  .tiles span:nth-child(2){opacity:.8}
  .tiles span:nth-child(3){opacity:.6}
  .tiles span:nth-child(4){opacity:.4}
  .tiles span:nth-child(5){opacity:.2}
</style>
</head>
<body>

  <section class="card card--back" aria-label="Card back">
    <svg class="band" width="760" height="434" viewBox="0 0 760 434" aria-hidden="true">
      <polygon points="0,150 470,150 490,132 490,280 0,280" fill="var(--band)"/>
      <rect x="500" y="132" width="46" height="148" fill="var(--stripe)"/>
      <rect x="560" y="132" width="46" height="148" fill="var(--stripe)" opacity=".8"/>
      <rect x="620" y="132" width="46" height="148" fill="var(--stripe)" opacity=".6"/>
      <rect x="680" y="132" width="46" height="148" fill="var(--stripe)" opacity=".4"/>
      <rect x="740" y="132" width="20" height="148" fill="var(--stripe)" opacity=".2"/>
    </svg>
    <div class="brand">
      <div class="brand__dot"></div>
      <div class="brand__text">
        <span class="brand__name">81M LLC</span>
        <span class="brand__tagline">life sciences advisory and compliance support</span>
      </div>
    </div>
    <p class="url">www.81mgroupconsulting.com</p>
  </section>

  <section class="card card--front" aria-label="Card front">
    <div class="brand">
      <div class="brand__dot"></div>
      <div class="brand__text">
        <span class="brand__name">81M LLC</span>
        <span class="brand__tagline">life sciences advisory and compliance support</span>
      </div>
    </div>
    <p class="contact contact--address">48, CD, UK, R3K 2V6<br>www.81mgroupconsulting.com</p>
    <p class="contact contact--direct">(555) 201. 4478<br>daniel@81mgroup.com</p>
    <div class="id-band">
      <div class="id-band__name">Daniel Marsh</div>
      <div class="id-band__title">CEO MANAGER</div>
    </div>
    <div class="tiles" aria-hidden="true"><span></span><span></span><span></span><span></span><span></span></div>
  </section>

</body>
</html>
```